New business card, letter head, email signature and Portfolio for our Security company.

We are an Elite security company that provides a top quality manpower services to protect high rise buildings, retail and all type of properties and would like a new business card/logo look.

- We would like the spot UV design.
- Matt black (double sided).
- We would like to incorporate a royal blue colour (feel free to experiment with it).
- Feel free to try different lengths with the card to make it stand out more than a normal business card.
- We would like the logo to be an eagle eye in the background (shines when card is tilted slightly in the background, either on the front, back or both sides of the card). Image attached as an example of eye shape (colour to be either black or royal blue).
- MAVRIN OAK GUARD PATROLS PTY. LTD. and MOGP to be placed on one side of the card and on the other side of the card to have;

- Name in slightly bigger font than the position (directly on the bottom on the name).
- Mobile number
- Email address
- Website email address
- PO BOX address

Can we please have the files in a format that we can edit.

Reason: I need to consult my business partner with the designs so far and will make a decision from there.

Target Market(s)

Security Industry

Industry/Entity Type

Business

Contact Information for Business Card

- Mobile number
- Email address
- Website email address
- PO BOX address

Logo Text

MOGP and underneath the MOGP please add MAVRIN OAK GUARD PATROLS PTY. LTD.

Font styles to use
Other font styles liked:
• bold type font

Colors
0255a3
000000

Requirements
Must have
• We are an Elite security company that provides a top quality manpower services to protect high rise buildings, retail and all type of properties and would like a new business card/logo look.
• - We would like the spot UV design.
• - Matt black (double sided).
• - We would like to incorporate a royal blue colour (feel free to experiment with it).
• - Feel free to try different lengths with the card to make it stand out more than a normal business card.
• - We would like the logo to be an eagle eye in the background (shines when card is tilted slightly in the background, either on the front, back or both sides of the card). Image attached as an example of eye shape (colour to be either black or royal blue).
• - MAVRIN OAK GUARD PATROLS PTY. LTD. and MOGP to be placed on one side of the card and on the other side of the card to have;
• - Name in slightly bigger font than the position (directly on the bottom on the name).
• - Mobile number
• - Email address
• - Website email address
• - PO BOX address
• Can we please have the files in a format that we can edit.
Nice to have
• Feel free to try different lengths with the card to make it stand out more than a normal business card.
• Please find "URBAN JUNGLE" font attached and incorporate MOGP into the same style with building's inside the MOGP bold front also add MAVRIN into the bottom part of the S and follow on E - Elite on the bottom S - SECURITY on the bottom S - SERVICES on the bottom of each letter.
• other than that, I'll be happy with a bold modern font for the MOGP and MAVRIN OAK GUARD PATROLS in a bold and thinner font underneath.

```html
<!DOCTYPE html>
<html lang="en">
<head>
<meta charset="utf-8">
<title>MOGP Business Card</title>
<link rel="stylesheet" href="https://fonts.googleapis.com/css2?family=Saira+Stencil+One&family=Open+Sans:wght@400&display=swap">
<style>
  :root {
    --card-bg: #222222;
    --accent-yellow: #fcc72c;
    --text-white: #ffffff;
    --mark-grey: #d4d4d4;
    --divider: #ffffff;
  }
  * { margin: 0; padding: 0; box-sizing: border-box; }
  html, body {
    width: 1050px;
    height: 1200px;
    overflow: hidden;
    background: var(--card-bg);
  }
  .sheet {
    position: relative;
    width: 1050px;
    height: 1200px;
    background: var(--card-bg);
  }
  .card-side {
    position: absolute;
    left: 0;
    width: 1050px;
  }
  .card-front { top: 0; height: 599px; }
  .card-back { top: 601px; height: 599px; }
  .divider {
    position: absolute;
    top: 598px;
    left: 0;
    width: 1050px;
    height: 3px;
    background: var(--divider);
  }
  .contact-block {
    position: absolute;
    right: 54px;
    top: 262px;
    text-align: right;
  }
  .person-name {
    font-family: "Saira Stencil One", sans-serif;
    font-size: 49px;
    line-height: 1;
    color: var(--accent-yellow);
    letter-spacing: 0.5px;
  }
  .person-position {
    font-family: "Saira Stencil One", sans-serif;
    font-size: 24px;
    line-height: 1;
    color: var(--text-white);
    margin-top: 2px;
    letter-spacing: 0.5px;
  }
  .contact-list {
    list-style: none;
    margin-top: 28px;
    font-family: "Open Sans", sans-serif;
    font-size: 22px;
    color: var(--text-white);
  }
  .contact-list li { line-height: 34px; }
  .contact-list li:last-child { line-height: 30px; }
  .brand-lockup {
    position: absolute;
    left: 0;
    top: 230px;
    width: 1050px;
    display: flex;
    flex-direction: column;
    align-items: center;
  }
  .brand-row {
    display: flex;
    align-items: center;
    gap: 22px;
  }
  .brand-dot {
    width: 70px;
    height: 70px;
    border-radius: 50%;
    background: var(--accent-yellow);
  }
  .brand-name {
    font-family: "Saira Stencil One", sans-serif;
    font-size: 170px;
    line-height: 0.95;
    color: var(--mark-grey);
    letter-spacing: 4px;
  }
  .brand-tagline {
    font-family: "Saira Stencil One", sans-serif;
    font-size: 30px;
    color: var(--mark-grey);
    letter-spacing: 1px;
    margin-top: 4px;
  }
</style>
</head>
<body>
  <main class="sheet">
    <section class="card-side card-front">
      <div class="contact-block">
        <h1 class="person-name">JOHN DOE</h1>
        <p class="person-position">POSITION</p>
        <ul class="contact-list">
          <li>09XXXXXXXXX</li>
          <li>XXXX@email.com</li>
          <li>XXXX@email.com</li>
          <li>PO BOX Address</li>
        </ul>
      </div>
    </section>
    <div class="divider"></div>
    <section class="card-side card-back">
      <div class="brand-lockup">
        <div class="brand-row">
          <span class="brand-dot"></span>
          <span class="brand-name">MOGP</span>
        </div>
        <p class="brand-tagline">MAVRIN OAK GUARD PATROLS</p>
      </div>
    </section>
  </main>
</body>
</html>
```